Cosmetic injections clinic needs a fresh looking business card

We need a business card using the supplied logo and color scheme to attract future clients to our clinic. It should be modern and fresh, eye catching and not too busy. Simple and to the point is best. I would like two sided designs with the front indicating address and contact information, and the back in full color with white logo and descriptive information also provided.
Target Market(s)
Clients looking for non surgical beauty enhancements.
Contact Information for Business Card
MeloraSkin
14, 618 Birchmont Way
St. Albert, Alberta
K2P 7W3
Phone: 587-412-6630
Email: info@meloraskin.com
Requirements
Must have
- -Logo supplied with the name and address of the clinic
- -Back of card in full color with white logo with A small line of text indicating both of the following: Anti aging consultants and cosmetic injectables
- Located inside the Voyager Wellness Group

```html
<!DOCTYPE html>
<html lang="en">
<head>
<meta charset="utf-8">
<title>MeloraSkin Business Card</title>
<link href="https://fonts.googleapis.com/css2?family=Source+Sans+3:wght@400;600&display=swap" rel="stylesheet">
<style>
  :root {
    --backdrop: #333333;
    --pink: #e44195;
    --purple: #6a479c;
    --teal: #33baa8;
    --white: #ffffff;
    --font: "Source Sans 3", "Myriad Pro", Arial, sans-serif;
  }
  * { margin: 0; padding: 0; box-sizing: border-box; }
  html, body { width: 1051px; height: 1200px; overflow: hidden; background: var(--backdrop); }
  body { position: relative; font-family: var(--font); color: var(--white); }

  .card { position: absolute; left: 23px; width: 1009px; overflow: hidden; }
  .card-front { top: 18px; height: 577px; background: var(--white); }
  .card-back { top: 615px; height: 575px; background: var(--pink); }

  .brand-header { position: absolute; top: 0; left: 0; width: 100%; height: 162px;
    display: flex; align-items: center; justify-content: center; gap: 14px; }
  .brand-dot { width: 30px; height: 30px; border-radius: 50%; background: var(--pink); }
  .brand-name { font-size: 54px; font-weight: 600; color: var(--purple); letter-spacing: 0.5px; }

  .band { position: absolute; left: 0; width: 100%; }
  .band-address { top: 162px; height: 212px; background: var(--pink); }
  .band-phone { top: 374px; height: 62px; background: var(--purple); }
  .band-email { top: 436px; height: 60px; background: var(--teal); }

  .contact-row { position: absolute; left: 0; width: 100%; }
  .contact-icon { position: absolute; }
  .contact-text { position: absolute; left: 422px; font-size: 29px; line-height: 39px; white-space: nowrap; }

  .address .contact-text { top: 36px; }
  .address .contact-icon { left: 356px; top: 44px; }
  .phone .contact-text { top: 11px; }
  .phone .contact-icon { left: 351px; top: 7px; }
  .email .contact-text { top: 11px; }
  .email .contact-icon { left: 354px; top: 13px; }

  .stripe { position: absolute; height: 9px; }
  .front-stripes { top: 498px; }
  .back-stripes { top: 496px; }
  .stripe-1 { left: 0; width: 336px; background: var(--teal); }
  .stripe-2 { left: 336px; width: 337px; background: var(--purple); }
  .stripe-3 { left: 673px; width: 336px; }
  .front-stripes .stripe-3 { background: var(--pink); }
  .back-stripes .stripe-3 { background: var(--white); }

  .back-brand { position: absolute; top: 200px; left: 0; width: 100%;
    display: flex; align-items: center; justify-content: center; gap: 24px; }
  .back-brand .brand-dot { width: 56px; height: 56px; background: var(--white); }
  .back-brand .brand-name { font-size: 112px; color: var(--white); }
  .tagline { position: absolute; top: 450px; left: 0; width: 100%; text-align: center; font-size: 22px; }
</style>
</head>
<body>
  <section class="card card-front">
    <header class="brand-header">
      <span class="brand-dot"></span>
      <span class="brand-name">MeloraSkin</span>
    </header>

    <div class="band band-address">
      <div class="contact-row address">
        <svg class="contact-icon" width="36" height="60" viewBox="0 0 36 60" aria-hidden="true">
          <path d="M18 0C8 0 0 8 0 18c0 12 18 42 18 42s18-30 18-42C36 8 28 0 18 0z" fill="#fff"/>
          <circle cx="18" cy="18" r="7" fill="#e44195"/>
        </svg>
        <p class="contact-text">MeloraSkin<br>14, 618 Birchmont Way<br>St. Albert, Alberta<br>K2P 7W3</p>
      </div>
    </div>

    <div class="band band-phone">
      <div class="contact-row phone">
        <svg class="contact-icon" width="46" height="46" viewBox="0 0 24 24" aria-hidden="true">
          <path fill="#fff" d="M6.6 10.8c1.4 2.8 3.8 5.1 6.6 6.6l2.2-2.2c.3-.3.7-.4 1-.2 1.1.4 2.3.6 3.6.6.6 0 1 .4 1 1V20c0 .6-.4 1-1 1C10.6 21 3 13.4 3 4c0-.6.4-1 1-1h3.5c.6 0 1 .4 1 1 0 1.3.2 2.5.6 3.6.1.3 0 .7-.2 1L6.6 10.8z"/>
        </svg>
        <p class="contact-text">Phone: 587-412-6630</p>
      </div>
    </div>

    <div class="band band-email">
      <div class="contact-row email">
        <svg class="contact-icon" width="46" height="32" viewBox="0 0 46 32" aria-hidden="true">
          <rect x="0" y="0" width="46" height="32" fill="#fff"/>
          <path d="M1 1 L23 20 L45 1" fill="none" stroke="#33baa8" stroke-width="2"/>
        </svg>
        <p class="contact-text">Email: info@meloraskin.com</p>
      </div>
    </div>

    <div class="front-stripes">
      <span class="stripe stripe-1"></span>
      <span class="stripe stripe-2"></span>
      <span class="stripe stripe-3"></span>
    </div>
  </section>

  <section class="card card-back">
    <div class="back-brand">
      <span class="brand-dot"></span>
      <span class="brand-name">MeloraSkin</span>
    </div>
    <p class="tagline">Anti aging consultants and cosmetic injectables</p>
    <div class="back-stripes">
      <span class="stripe stripe-1"></span>
      <span class="stripe stripe-2"></span>
      <span class="stripe stripe-3"></span>
    </div>
  </section>
</body>
</html>
```